Brackenfold Latches Business Cards

Need high quality business card designed around my company logo. Ideally the cards need to be a glossy black as the logo goes well with a black background.

The company is a Locksmithing business.

Domestic clients are Residential Home Owners and Landlords. Commercial clients are local businesses, estate agents, landlords, solicitors

Services offered :
Emergency Lock Out
New Lock Fitting & Replacement
High Security Upgrades
UPVC lock repairs
Mobile Key Cutting
Free Security Reviews

Qualificatons & Certifications:
Accredited Guild & Tower KSR Level 3, QTRB
Fully Insured
PVX Checked

Contact & Business Details:

Business Name : Brackenfold Latches
Name: Rob Fenwick
Tel: 01823 574419 Office / 07841592637 Mobile
Email: contact@brackenfoldlatches.com
Website: www.brackenfoldlatches.com

(please note that the website is currently under development and not available to view)

Locksmith

Name: Rob Fenwick

Services:
Emergency Lock Out
High Security Upgrades
UPVC lock repairs
Mobile Key Cutting
Free Security Reviews

• Ideally the cards should be a glossy black as the logo stands out better on a black background.

Logo on front and the word LOCKSMITH should be incorporated into the front design of the card.

Qualifications & Certifications on the back ideally along the top / bottom of the card or split (I.e along the top “ Accredited : Guild & Tower Level 3 , QTRB”
and along the bottom , “Fully Insured & PVX Checked”

Services offered ideally listed on the back of the card, preferably split into two columns. If possible the logo could also be incorporated onto the back of the card between the two services columns (I.e the services listed either side of the logo)
• On the back of the card, have the logo in the middle with the services listed either side of the logo I.e 3 services on left of logo and three to the right.

```html
<!DOCTYPE html>
<html lang="en">
<head>
<meta charset="utf-8">
<title>Brackenfold Latches – Business Cards</title>
<link href="https://fonts.googleapis.com/css2?family=Michroma&family=Outfit:wght@400;500;600&display=swap" rel="stylesheet">
<style>
  :root {
    --page: #ffffff;
    --card: #000000;
    --gold: #c4942c;
    --gold-light: #e0b64a;
    --white: #ffffff;
  }
  * { margin: 0; padding: 0; box-sizing: border-box; }
  html, body { width: 1200px; height: 1200px; overflow: hidden; background: var(--page); }
  body { position: relative; font-family: "Outfit", sans-serif; }

  .card {
    position: absolute;
    left: 216px;
    width: 775px;
    height: 431px;
    background: var(--card);
    color: var(--white);
  }
  .card--front { top: 153px; }
  .card--back { top: 624px; }

  /* brand mark */
  .brand {
    position: absolute;
    display: flex;
    align-items: center;
    justify-content: center;
    border: 2px solid var(--gold);
    border-radius: 50%;
    text-align: center;
    color: var(--gold);
    font-family: "Outfit", sans-serif;
    font-weight: 600;
    line-height: 1.1;
    text-transform: uppercase;
    letter-spacing: 1px;
  }
  .card--front .brand { left: 81px; top: 44px; width: 152px; height: 152px; font-size: 19px; }
  .card--back .brand { left: 292px; top: 143px; width: 190px; height: 190px; font-size: 23px; }

  .headline {
    position: absolute;
    font-family: "Michroma", sans-serif;
    text-transform: uppercase;
    white-space: nowrap;
  }
  .locksmith {
    left: 157px; top: 212px;
    transform: translateX(-50%);
    font-size: 23px;
    color: var(--gold);
    letter-spacing: 1px;
  }
  .person-name {
    right: 22px; top: 240px;
    font-size: 24px;
    letter-spacing: 1px;
  }
  .person-name .surname { color: var(--gold); }
  .person-role {
    right: 21px; top: 272px;
    font-size: 13px;
    letter-spacing: 2px;
  }
  .rule {
    position: absolute;
    height: 2px;
    background: var(--white);
  }
  .rule--gold { background: var(--gold); }
  .front-rule { left: 22px; top: 281px; width: 583px; }

  .contacts {
    position: absolute;
    left: 54px; top: 296px;
    list-style: none;
  }
  .contacts li {
    display: flex;
    align-items: center;
    height: 28px;
    font-size: 18px;
    font-weight: 400;
  }
  .contacts svg {
    width: 17px; height: 17px;
    margin-right: 12px;
    fill: none;
    stroke: var(--gold);
    stroke-width: 2;
  }
  .contacts .solid { fill: var(--gold); stroke: none; }

  /* back */
  .cert {
    position: absolute;
    left: 0; right: 0;
    display: flex;
    align-items: center;
    justify-content: center;
    gap: 14px;
    font-family: "Michroma", sans-serif;
    color: var(--gold);
    white-space: nowrap;
  }
  .cert::before, .cert::after {
    content: "";
    height: 2px;
    background: var(--gold);
  }
  .cert--top { top: 35px; font-size: 17px; }
  .cert--top::before, .cert--top::after { width: 36px; }
  .cert--bottom { top: 369px; font-size: 18px; gap: 20px; }
  .cert--bottom::before, .cert--bottom::after { width: 130px; }

  .section-title {
    position: absolute;
    left: 0; right: 0; top: 88px;
    text-align: center;
    font-size: 16px;
    letter-spacing: 3px;
    font-weight: 500;
  }
  .section-rule-left { left: 19px; top: 97px; width: 263px; }
  .section-rule-right { left: 493px; top: 97px; width: 263px; }

  .services {
    position: absolute;
    list-style: none;
    font-size: 19px;
    line-height: 1.35;
  }
  .services li {
    position: absolute;
    left: 28px;
    white-space: nowrap;
  }
  .services li::before {
    content: "";
    position: absolute;
    left: -28px; top: 13px;
    width: 11px; height: 3px;
    background: var(--gold);
  }
  .services--left { left: 29px; top: 173px; }
  .services--right { left: 506px; top: 173px; }
</style>
</head>
<body>

<section class="card card--front">
  <div class="brand">Brackenfold<br>Latches</div>
  <div class="headline locksmith">Locksmith</div>
  <div class="headline person-name">Rob <span class="surname">Fenwick</span></div>
  <div class="headline person-role">CEO/Owner</div>
  <div class="rule front-rule"></div>
  <ul class="contacts">
    <li>
      <svg viewBox="0 0 24 24"><path class="solid" d="M6.6 10.8a15 15 0 0 0 6.6 6.6l2.2-2.2a1 1 0 0 1 1-.25 11.4 11.4 0 0 0 3.6.6 1 1 0 0 1 1 1V20a1 1 0 0 1-1 1A17 17 0 0 1 3 4a1 1 0 0 1 1-1h3.5a1 1 0 0 1 1 1c0 1.25.2 2.45.6 3.6a1 1 0 0 1-.25 1z"/></svg>
      018 - 2357 - 4419
    </li>
    <li>
      <svg viewBox="0 0 24 24"><path class="solid" d="M2 9c2-3 6-4 10-4s8 1 10 4l-3 2-2-2V7H7v2l-2 2zM6 12h12l2 8H4zm6 2.5a2.5 2.5 0 1 0 0 5 2.5 2.5 0 0 0 0-5z"/></svg>
      078 - 4159 - 2637
    </li>
    <li>
      <svg viewBox="0 0 24 24"><circle cx="12" cy="12" r="10"/><ellipse cx="12" cy="12" rx="4.5" ry="10"/><path d="M2 12h20M4 7h16M4 17h16"/></svg>
      www.brackenfoldlatches.com
    </li>
    <li>
      <svg viewBox="0 0 24 24"><rect x="2" y="5" width="20" height="14"/><path d="M2 5l10 8 10-8M2 19l7-7M22 19l-7-7"/></svg>
      contact@brackenfoldlatches.com
    </li>
  </ul>
</section>

<section class="card card--back">
  <div class="cert cert--top">Accredited Guild &amp; Tower KSR Level 3, QTRB</div>
  <div class="rule section-rule-left"></div>
  <div class="section-title">OUR SERVICES</div>
  <div class="rule section-rule-right"></div>

  <ul class="services services--left">
    <li style="top:0">Emergency Lock Out</li>
    <li style="top:35px">New Lock Fitting &amp;<br>Replacement</li>
    <li style="top:93px">High Security Upgrades</li>
  </ul>

  <div class="brand">Brackenfold<br>Latches</div>

  <ul class="services services--right">
    <li style="top:0">UPVC lock repairs</li>
    <li style="top:46px">Mobile Key Cutting</li>
    <li style="top:93px">Free Security Reviews</li>
  </ul>

  <div class="cert cert--bottom">Fully Insured &amp; PVX Checked</div>
</section>

</body>
</html>
```